R&T Cleanwave Stripping Business Card

We are in need of a business card design for our new Texas based company called 'R&T Cleanwave Stripping'. Our new innovative mobile media blasting service utilizes recycled material and a new water based process that eliminates all dust (i.e. as apposed to the old sand blasting format). Our 'advanced surface preparation' service targets multiple industries such as automotive, Industrial, marine and structural (graffiti removal). We would like to see the design include a recycling type logo or concept that utilizes colors such as black, various shades of green, some white, yellow and/or grey (e.g. perhaps a blackish background). The final design should look simple and professional and should clearly communicate the environmentally friendly approach through logo or design (i.e. Eco-Friendly, Go Green or Blast Green methodologies). Thank you in advance!
Updates

Please pardon any inconvenience. We have decided to pursue a two sided business card. All original information/designs requirements remains the same for the front. However, we would like back of the card to state the following: "We bring the power of Hydroveil Media Scouring equipment to your location. We can remove any coating from any surface. Bullets include: Paint Stripping, Auto Restoration, Graffiti Removal, Black Walls & Stone, Concrete, Boats, Iron Fences, Tractors & Trailers, Pools & Fountains, Wood Restoration.

Industry/Entity Type

Recycling

Contact Information for Business Card

R&T Cleanwave Stripping, LLC - Gordon Pelly, MBA, PMP - cell: 915-382-6091, office: 915-627-8853 - gpelly@rtcleanwavestripping.com - CEO/Founder

Requirements
Must have
• Recycle or environmentally friendly logos or design.
Nice to have
• Business oriented design with an aggressive look. Also, if possible would like to see R&T incorporated into the design or logo. Please note that we have decided to add the option of adding details to the back of the card (2 sided). The front should contain the logo/design and the back should have the following details listed: "We bring the power of Hydroveil Media Scouring equipment to your location. We can remove any coating from any surface. Bullets include: Paint Stripping, Auto Restoration, Graffiti Removal, Black Walls & Stone, Concrete, Boats, Iron Fences, Tractors & Trailers, Pools & Fountains, Wood Restoration.

```html
<!DOCTYPE html>
<html lang="en">
<head>
<meta charset="utf-8">
<title>R&amp;T Cleanwave Stripping – Business Card</title>
<link href="https://fonts.googleapis.com/css2?family=Quicksand:wght@500;600;700&display=swap" rel="stylesheet">
<style>
  :root {
    --bg-light: #8cc21a;
    --bg-dark: #2f7f0a;
    --card: #1b1b1b;
    --lime: #c9e63a;
    --green: #2fae55;
    --deep-green: #1e5a3e;
  }
  * { margin: 0; padding: 0; box-sizing: border-box; }
  html, body { width: 1200px; height: 849px; overflow: hidden; }
  body {
    background: radial-gradient(ellipse at 40% 30%, var(--bg-light), var(--bg-dark));
    font-family: "Quicksand", sans-serif;
    position: relative;
  }
  .card {
    position: absolute;
    top: 275px;
    width: 525px;
    height: 300px;
    background: var(--card);
    border-radius: 4px;
    overflow: hidden;
    box-shadow: 0 10px 28px rgba(0,0,0,0.35);
  }
  .card-front { left: 50px; }
  .card-back { left: 625px; }

  .brand { display: flex; align-items: center; gap: 8px; }
  .brand-dot {
    width: 30px; height: 30px; border-radius: 50%;
    background: var(--green);
  }
  .brand-text { display: flex; flex-direction: column; }
  .brand-name { color: var(--lime); font-weight: 700; font-size: 30px; line-height: 1; }
  .brand-sub { color: var(--green); font-weight: 600; font-size: 12px; margin-top: 2px; }

  /* Front */
  .card-front .brand { position: absolute; left: 30px; top: 28px; }
  .contact { position: absolute; left: 30px; top: 110px; }
  .person-name { color: var(--lime); font-size: 21px; font-weight: 600; }
  .person-name .credentials { font-size: 12px; color: var(--green); }
  .person-title { color: var(--green); font-size: 13px; font-weight: 600; margin-bottom: 10px; }
  .contact-line { font-size: 13px; font-weight: 600; line-height: 1.45; color: var(--lime); }
  .contact-line .label { color: var(--green); }
  .front-deco { position: absolute; right: -70px; bottom: -120px; }

  /* Back */
  .card-back .brand { position: absolute; left: 210px; top: 24px; }
  .tagline {
    position: absolute; left: 0; right: 0; top: 84px;
    text-align: center; color: var(--lime);
    font-size: 13.5px; font-weight: 700; line-height: 1.35;
  }
  .services {
    position: absolute; top: 150px; list-style: none;
  }
  .services-left { left: 48px; }
  .services-right { left: 290px; }
  .services li {
    display: flex; align-items: center; gap: 7px;
    color: var(--green); font-size: 13.5px; font-weight: 600; line-height: 1.5;
  }
  .services li::before {
    content: ""; width: 9px; height: 9px; border-radius: 50%;
    background: var(--lime); flex: none;
  }
</style>
</head>
<body>
  <section class="card card-front">
    <div class="brand">
      <span class="brand-dot"></span>
      <div class="brand-text">
        <span class="brand-name">R&amp;T</span>
        <span class="brand-sub">Cleanwave Stripping, LLC</span>
      </div>
    </div>
    <div class="contact">
      <p class="person-name">Gordon Pelly<span class="credentials">, MBA, PMP</span></p>
      <p class="person-title">CEO/Founder</p>
      <p class="contact-line"><span class="label">Cell:</span> 915-382-6091</p>
      <p class="contact-line"><span class="label">Office:</span> 915-627-8853</p>
      <p class="contact-line"><span class="label">E-mail:</span> gpelly@rtcleanwavestripping.com</p>
    </div>
    <svg class="front-deco" width="300" height="300" viewBox="0 0 300 300" aria-hidden="true">
      <circle cx="150" cy="150" r="150" fill="var(--deep-green)"/>
    </svg>
  </section>

  <section class="card card-back">
    <div class="brand">
      <span class="brand-dot"></span>
      <div class="brand-text">
        <span class="brand-name">R&amp;T</span>
        <span class="brand-sub">Cleanwave Stripping, LLC</span>
      </div>
    </div>
    <p class="tagline">We bring the power of<br>Hydroveil Media Scouring equipment to your location.<br>We can remove any coating from any surface.</p>
    <ul class="services services-left">
      <li>Paint Stripping</li>
      <li>Auto Restoration</li>
      <li>Graffiti Removal</li>
      <li>Black Walls &amp; Stone</li>
      <li>Concrete</li>
    </ul>
    <ul class="services services-right">
      <li>Boats</li>
      <li>Iron Fences</li>
      <li>Tractors &amp; Trailers</li>
      <li>Pools &amp; Fountains</li>
      <li>Wood Restoration</li>
    </ul>
  </section>
</body>
</html>
```